Business Card Design

Needing a business card design similar to the business card that is attached.

Industry/Entity Type

Business

Contact Information for Business Card

Design similar to the b-cards that is attached.

```html
<!DOCTYPE html>
<html lang="en">
<head>
<meta charset="utf-8">
<title>Business Cards</title>
<link rel="stylesheet" href="https://fonts.googleapis.com/css2?family=Tinos:wght@400;700&display=swap">
<style>
  :root {
    --page-bg: #ece8e2;
    --card-bg: #ffffff;
    --ink: #1b1b1b;
    --accent-blue: #3a59b8;
    --accent-red: #e0262b;
    --brand-green: #3fae2a;
    --brand-red: #d9262c;
    --brand-teal: #2a9fd0;
    --card-shadow: rgba(0, 0, 0, 0.18);
  }
  * { margin: 0; padding: 0; box-sizing: border-box; }
  html, body {
    width: 1200px;
    height: 784px;
    overflow: hidden;
    background: var(--page-bg);
    font-family: "Tinos", "Times New Roman", serif;
    color: var(--ink);
  }
  .canvas { position: relative; width: 1200px; height: 784px; }
  .card {
    position: absolute;
    width: 560px;
    height: 320px;
    background: var(--card-bg);
    box-shadow: 0 6px 18px var(--card-shadow);
  }
  .card--thermal { left: 70px; top: 70px; }
  .card--realty { left: 570px; top: 394px; }

  .brand {
    position: absolute;
    display: flex;
    align-items: center;
    gap: 12px;
    font-weight: 700;
    font-size: 34px;
    white-space: nowrap;
  }
  .brand__mark { flex: none; }
  .card--thermal .brand { left: 38px; top: 38px; color: var(--brand-green); font-size: 32px; }
  .card--realty .brand { left: 40px; top: 42px; color: var(--brand-red); }

  .person {
    position: absolute;
    text-align: center;
    font-size: 20px;
    line-height: 1.2;
  }
  .person__role { color: var(--accent-blue); font-size: 17px; }
  .person__phone { color: var(--accent-red); font-size: 19px; }
  .card--thermal .person { left: 170px; top: 104px; width: 300px; }
  .card--realty .person { left: 190px; top: 112px; width: 200px; }

  .address {
    position: absolute;
    font-size: 21px;
    line-height: 1.25;
    font-style: normal;
  }
  .card--thermal .address { left: 40px; top: 212px; }
  .card--realty .address { left: 42px; top: 222px; }

  .contact {
    position: absolute;
    font-size: 18px;
    line-height: 1.28;
    text-align: center;
  }
  .contact__web { color: var(--accent-red); }
  .card--thermal .contact { left: 320px; top: 182px; width: 220px; }
  .card--realty .contact { left: 300px; top: 196px; width: 240px; }
</style>
</head>
<body>
<main class="canvas">

  <section class="card card--thermal">
    <div class="brand">
      <svg class="brand__mark" width="44" height="44" viewBox="0 0 44 44" aria-hidden="true">
        <circle cx="22" cy="22" r="20" fill="var(--brand-green)"/>
      </svg>
      <span>NorthRidgeThermal,Inc.com</span>
    </div>
    <div class="person">
      <p class="person__name">Daniel Tesfaye</p>
      <p class="person__role">M.E &amp; Certified Geothermal Installer</p>
      <p class="person__phone">(206) 555-0148</p>
    </div>
    <address class="address">4210 S 188th St. # B200<br>Renton, WA 98055</address>
    <div class="contact">
      <p>To learn about Geo</p>
      <p>Visit our Website:</p>
      <p class="contact__web">NorthRidgeThermalinc.com</p>
    </div>
  </section>

  <section class="card card--realty">
    <div class="brand">
      <svg class="brand__mark" width="46" height="46" viewBox="0 0 46 46" aria-hidden="true">
        <rect x="2" y="2" width="42" height="42" fill="var(--brand-teal)"/>
      </svg>
      <span>Harborline Realty, Inc.com</span>
    </div>
    <div class="person">
      <p class="person__name">Daniel Tesfaye</p>
      <p class="person__role">Broker</p>
      <p class="person__phone">(206) 555-0148</p>
    </div>
    <address class="address">4210 S 188th St. # B200<br>Renton, WA 98055</address>
    <div class="contact">
      <p>Phone: (206) 555-0148</p>
      <p>Fax: (253) 555-0172</p>
      <p class="contact__web">HarborlineRealtyinc.com</p>
    </div>
  </section>

</main>
</body>
</html>
```